Vorbly BIZ Card, email signature & Stationary

Professional business cards, email signatures and ms word letterhead

Target Market(s)

business owners

Industry/Entity Type

cloud hosting

Contact Information for Business Card

name title office phone number , direct line, fax email address web site

Font styles to use
Other font styles liked:
• something that compliments font in logo

```html
<!DOCTYPE html>
<html lang="en">
<head>
<meta charset="UTF-8">
<title>Vorbly Business Card</title>
<link rel="stylesheet" href="https://fonts.googleapis.com/css2?family=Poppins:wght@300;400;700&display=swap">
<style>
  :root {
    --page-bg: #d9d9d9;
    --card-bg: #262626;
    --accent-red: #e3161f;
    --logo-silver: #bdbdbd;
    --text-light: #f2f2f2;
    --text-muted: #cfcfcf;
  }
  * { margin: 0; padding: 0; box-sizing: border-box; }
  html, body {
    width: 1200px;
    height: 900px;
    overflow: hidden;
    background: var(--page-bg);
    font-family: 'Poppins', sans-serif;
  }
  .canvas {
    position: relative;
    width: 1200px;
    height: 900px;
  }
  .card {
    position: absolute;
    left: 320px;
    width: 560px;
    height: 320px;
    background: var(--card-bg);
    border-radius: 22px;
    overflow: hidden;
  }
  .card--front {
    top: 100px;
    border-bottom: 5px solid var(--accent-red);
  }
  .card--back { top: 480px; }

  .brand {
    font-weight: 300;
    letter-spacing: -2px;
    line-height: 1;
    display: flex;
    align-items: center;
    gap: 14px;
  }
  .brand__mark {
    width: 14px;
    height: 14px;
  }
  .card--front .brand {
    position: absolute;
    left: 0; right: 0; top: 0; bottom: 0;
    justify-content: center;
    font-size: 104px;
    color: var(--logo-silver);
  }
  .card--front .brand__mark { background: var(--logo-silver); }

  .card--back .brand {
    position: absolute;
    left: 34px;
    top: 118px;
    font-size: 72px;
    color: var(--accent-red);
  }
  .card--back .brand__mark { background: var(--accent-red); width: 11px; height: 11px; }

  .divider {
    position: absolute;
    left: 300px;
    top: 70px;
    width: 2px;
    height: 180px;
    background: var(--accent-red);
  }
  .contact {
    position: absolute;
    left: 322px;
    top: 72px;
    color: var(--text-light);
  }
  .contact__name {
    font-weight: 700;
    font-size: 17px;
    color: var(--accent-red);
    letter-spacing: 0.3px;
  }
  .contact__title {
    font-weight: 300;
    font-size: 13px;
    color: var(--text-muted);
    margin-bottom: 12px;
  }
  .contact__address {
    font-size: 12.5px;
    line-height: 1.35;
    margin-bottom: 12px;
  }
  .contact__list { list-style: none; font-size: 12.5px; }
  .contact__item {
    display: flex;
    align-items: center;
    gap: 10px;
    line-height: 1.65;
  }
  .contact__icon { width: 12px; height: 12px; flex: none; }
</style>
</head>
<body>
<main class="canvas">
  <section class="card card--front" aria-label="Card front">
    <div class="brand"><span class="brand__mark"></span>Vorbly</div>
  </section>

  <section class="card card--back" aria-label="Card back">
    <div class="brand"><span class="brand__mark"></span>Vorbly</div>
    <div class="divider"></div>
    <div class="contact">
      <p class="contact__name">DANIEL REYES</p>
      <p class="contact__title">Comercial</p>
      <p class="contact__address">Parque Norte, C/ 4 nº 22<br>28100 Villanueva del Río<br>Apartado de correos 312</p>
      <ul class="contact__list">
        <li class="contact__item">
          <svg class="contact__icon" viewBox="0 0 12 12"><path fill="var(--accent-red)" d="M1 4c0-2 1-3 5-3s5 1 5 3l-2 1-1-1.5H4L3 5zM3 6h6l1 5H2z"/></svg>
          910 44 27 15
        </li>
        <li class="contact__item">
          <svg class="contact__icon" viewBox="0 0 12 12"><rect x="3" y="0.5" width="6" height="11" rx="1" fill="none" stroke="var(--accent-red)" stroke-width="1.3"/><circle cx="6" cy="9.5" r="0.7" fill="var(--accent-red)"/></svg>
          655 18 39 04
        </li>
        <li class="contact__item">
          <svg class="contact__icon" viewBox="0 0 12 12"><rect x="3" y="1" width="6" height="4" fill="var(--accent-red)"/><rect x="1" y="5" width="10" height="6" rx="1" fill="var(--accent-red)"/></svg>
          910 44 27 80
        </li>
        <li class="contact__item">
          <svg class="contact__icon" viewBox="0 0 12 12"><rect x="0.5" y="2.5" width="11" height="7" fill="var(--accent-red)"/><path d="M0.5 2.5 6 6.5l5.5-4" fill="none" stroke="var(--card-bg)" stroke-width="1"/></svg>
          info@vorbly.com
        </li>
      </ul>
    </div>
  </section>
</main>
</body>
</html>
```